business card design

i would like business cards designed. My business provides trade qualified personnel to the mining industry to work on heavy mobile equipment.
please put a excavator(digger) in the background in one design and have one design without so i can compare the difference.
also add info:
my logo(attached) and "mobile equipment repair and maintenance"
name: Derek Holloway
address: 57 Tarrowby RD Carmel Perth WA.
mobile: 0438120957
email: derek@ironvalemx.com

```html
<!DOCTYPE html>
<html lang="en">
<head>
<meta charset="utf-8">
<title>Ironvale Maintenance Services – Business Cards</title>
<link href="https://fonts.googleapis.com/css2?family=Montserrat:wght@700;800;900&family=Roboto:wght@400;500;700&display=swap" rel="stylesheet">
<style>
  :root {
    --navy: #0c1f3f;
    --navy-deep: #0a1a36;
    --blue: #4172b8;
    --blue-light: #5b8ad0;
    --ink: #1c1f24;
    --paper: #ffffff;
    --page: #ffffff;
  }
  * { margin: 0; padding: 0; box-sizing: border-box; }
  html, body {
    width: 1200px; height: 1200px; overflow: hidden;
    background: var(--page);
  }
  .card {
    position: absolute;
    left: 239px;
    width: 730px;
    height: 417px;
    overflow: hidden;
    box-shadow: 10px 14px 18px rgba(0,0,0,0.35);
  }
  .card-front { top: 142px; background: var(--navy); }
  .card-back { top: 649px; background: var(--paper); }

  .card-graphics { position: absolute; inset: 0; width: 100%; height: 100%; }

  .wordmark {
    position: absolute;
    font-family: "Montserrat", sans-serif;
    font-weight: 900;
    line-height: 1;
    letter-spacing: 0.06em;
    white-space: nowrap;
  }
  .company-line {
    position: absolute;
    font-family: "Montserrat", sans-serif;
    font-weight: 700;
    color: var(--blue);
    letter-spacing: 0.07em;
    line-height: 1;
    white-space: nowrap;
  }
  .card-front .wordmark {
    left: 263px; top: 184px;
    font-size: 54px; color: var(--paper);
    width: 355px; text-align: center;
  }
  .card-front .company-line {
    left: 263px; top: 237px; width: 355px; text-align: center;
    font-size: 14px;
  }
  .card-back .wordmark {
    left: 31px; top: 32px;
    font-size: 62px; color: var(--navy);
  }
  .card-back .company-line {
    left: 77px; top: 94px; font-size: 15.5px;
  }

  .contact {
    position: absolute; left: 31px; top: 200px;
    font-family: "Roboto", sans-serif; color: var(--ink);
  }
  .contact-name {
    font-size: 24px; font-weight: 700; letter-spacing: 0.01em;
    margin-bottom: 26px;
  }
  .contact-address { font-size: 19px; font-weight: 500; margin-bottom: 24px; }
  .contact-row {
    display: flex; align-items: center; gap: 10px;
    font-size: 19px; font-weight: 500; height: 25px;
  }
  .contact-row svg { width: 15px; height: 15px; flex: none; }

  .tagline {
    position: absolute; left: 34px; top: 384px;
    font-family: "Roboto", sans-serif; font-weight: 500;
    font-size: 20px; color: var(--paper); line-height: 24px;
  }
</style>
</head>
<body>

<section class="card card-front" aria-label="Card front">
  <svg class="card-graphics" viewBox="0 0 730 417" preserveAspectRatio="none" aria-hidden="true">
    <defs>
      <linearGradient id="front-shade" x1="0" y1="1" x2="1" y2="0">
        <stop offset="0" stop-color="#0a1a36"/>
        <stop offset="1" stop-color="#0f2448"/>
      </linearGradient>
      <linearGradient id="band-glow" x1="0" y1="1" x2="1" y2="0">
        <stop offset="0" stop-color="#0c1f3f" stop-opacity="0"/>
        <stop offset="1" stop-color="#4172b8"/>
      </linearGradient>
    </defs>
    <rect width="730" height="417" fill="url(#front-shade)"/>
    <polygon points="227,0 361,0 288,107 155,107" fill="url(#band-glow)" opacity="0.7"/>
    <polygon points="411,0 545,0 472,107 339,107" fill="url(#band-glow)" opacity="0.85"/>
    <polygon points="595,0 730,0 656,107 523,107" fill="url(#band-glow)"/>
  </svg>
  <div class="wordmark">IRONVALE</div>
  <div class="company-line">MAINTENANCE SERVICES PTY LTD</div>
</section>

<section class="card card-back" aria-label="Card back">
  <svg class="card-graphics" viewBox="0 0 730 417" preserveAspectRatio="none" aria-hidden="true">
    <polygon points="0,375 475,375 448,417 0,417" fill="var(--navy)"/>
    <polygon points="503,375 581,375 552,417 473,417" fill="var(--blue)"/>
    <polygon points="601,375 681,375 650,417 571,417" fill="var(--blue)"/>
  </svg>

  <div class="wordmark">IRONVALE</div>
  <div class="company-line">MAINTENANCE SERVICES PTY LTD</div>

  <div class="contact">
    <div class="contact-name">DEREK HOLLOWAY</div>
    <div class="contact-address">57 Tarrowby RD Carmel Perth WA</div>
    <div class="contact-row">
      <svg viewBox="0 0 16 16" aria-hidden="true"><path d="M4.2 1.2 6 4.4 4.8 5.6c.7 2.2 2.4 4.2 4.6 5.3l1.3-1.2 3.1 1.9-1.2 2.6C8.2 14 2.4 8 2.2 3z" fill="var(--blue)"/></svg>
      <span>0438120957</span>
    </div>
    <div class="contact-row">
      <svg viewBox="0 0 16 16" aria-hidden="true"><rect x="1" y="3" width="14" height="10" fill="var(--blue)"/><path d="M1 3 8 9 15 3M1 13 6 7.5M15 13 10 7.5" stroke="#fff" stroke-width="1.2" fill="none"/></svg>
      <span>derek@ironvalemx.com</span>
    </div>
  </div>

  <div class="tagline">mobile equipment repair and maintenance</div>
</section>

</body>
</html>
```